Profesional personal website needs design and business card

I need a business card with my professional name as a logo "Marlo Vitality" for my business. I am a Wellness Coach, consultant and trainer. So it should be professional, wellness oriented and modern.

Target Market(s)

Private clients, governments, corporations. Luxury and high market.

Industry/Entity Type

Health And Wellness

Contact Information for Business Card

Marlo Vitality should be the logo

Colors

Designer to choose colors to be used in the design.

Requirements
Must have
• Marlo Vitality
• Name: Tomás Arribal
• Wellness Coach, Consultant & Trainer.
• Website: www.marlovitality.example
• Phone:
• Spain (+34) 612 480 397
• (USA) +1 (555) 318 2046
Nice to have
• The most important is the design of "Marlo Vitality", as this is going to be my personal brand logo. It should be professional, wellness, high end and actual.
Should not have
• no golds, no baroque style..

```html
<!DOCTYPE html>
<html lang="en">
<head>
<meta charset="utf-8">
<title>Marlo Vitality — Business Card</title>
<link rel="stylesheet" href="https://fonts.googleapis.com/css2?family=Roboto:wght@400;500;700&display=swap">
<style>
  :root {
    --stage: #2b2b2d;
    --slate: #46536a;
    --paper: #ffffff;
    --ink-navy: #3f4b63;
    --ink-brown: #3d2e1c;
    --role: #4f8a5a;
    --rule: #6b5a4a;
    --bar: #4d3a1c;
    --leaf: #4f9a4a;
    --body: #2a2a2a;
    --phone-rule: #9cc79a;
  }
  * { box-sizing: border-box; margin: 0; padding: 0; }
  html, body { width: 1200px; height: 880px; overflow: hidden; }
  body {
    background: var(--stage);
    font-family: "Roboto", Arial, sans-serif;
    position: relative;
  }
  .card {
    position: absolute;
    width: 560px;
    height: 320px;
    box-shadow: 0 10px 30px rgba(0,0,0,.45);
  }

  /* Back side */
  .card--back {
    left: 100px; top: 80px;
    background: var(--slate);
    color: #fff;
  }
  .card--back .brand {
    position: absolute;
    left: 0; right: 0; top: 112px;
    text-align: center;
    font-weight: 700;
    font-size: 44px;
    line-height: 52px;
    letter-spacing: .5px;
  }
  .card--back .url-spaced {
    position: absolute;
    left: 0; right: 0; bottom: 44px;
    text-align: center;
    font-size: 11px;
    letter-spacing: 9px;
    text-transform: uppercase;
  }

  /* Front side */
  .card--front {
    left: 540px; top: 480px;
    background: var(--paper);
  }
  .edge-bar {
    position: absolute;
    width: 6px;
    background: var(--bar);
  }
  .edge-bar--right { right: 0; top: 64px; height: 68px; }
  .edge-bar--left { left: 0; bottom: 20px; height: 72px; }
  .card--front .brand {
    position: absolute;
    right: 48px; top: 44px;
    font-weight: 700;
    font-size: 40px;
    line-height: 48px;
    color: var(--ink-navy);
    display: flex; align-items: center; gap: 10px;
  }
  .brand-dot {
    width: 12px; height: 12px; border-radius: 50%;
    background: var(--leaf);
  }
  .top-rule {
    position: absolute;
    left: 180px; right: 30px; top: 132px;
    height: 1px; background: var(--rule);
  }
  .website {
    position: absolute;
    right: 40px; top: 146px;
    display: flex; align-items: center; gap: 10px;
    font-size: 15px; color: var(--body);
  }
  .identity {
    position: absolute;
    left: 40px; top: 196px;
  }
  .identity .person {
    font-weight: 700; font-size: 24px; line-height: 28px; color: var(--ink-brown);
  }
  .identity .role {
    font-size: 15px; line-height: 19px; color: var(--role); margin-top: 2px;
  }
  .identity .name-rule {
    width: 330px; height: 1px; background: var(--rule); margin-top: 8px;
  }
  .phones {
    position: absolute;
    left: 56px; top: 266px;
    display: flex; align-items: center; gap: 12px;
  }
  .phones .divider { width: 1px; height: 38px; background: var(--phone-rule); }
  .phones ul { list-style: none; font-size: 14px; color: var(--body); line-height: 19px; }
</style>
</head>
<body>
  <section class="card card--back" aria-label="Card back">
    <div class="brand">Marlo Vitality</div>
    <div class="url-spaced">www.marlovitality.example</div>
  </section>

  <section class="card card--front" aria-label="Card front">
    <span class="edge-bar edge-bar--right"></span>
    <span class="edge-bar edge-bar--left"></span>
    <div class="brand"><span class="brand-dot"></span>Marlo Vitality</div>
    <div class="top-rule"></div>
    <div class="website">
      <svg width="18" height="18" viewBox="0 0 20 20" fill="none" stroke="#4f9a4a" stroke-width="1.6" aria-hidden="true">
        <circle cx="10" cy="10" r="8"/>
        <ellipse cx="10" cy="10" rx="3.5" ry="8"/>
        <line x1="2" y1="10" x2="18" y2="10"/>
        <line x1="3.5" y1="6" x2="16.5" y2="6"/>
        <line x1="3.5" y1="14" x2="16.5" y2="14"/>
      </svg>
      <span>www.marlovitality.example</span>
    </div>
    <div class="identity">
      <div class="person">Tomás Arribal</div>
      <div class="role">Wellness Coach, Consultant &amp; Trainer</div>
      <div class="name-rule"></div>
    </div>
    <div class="phones">
      <svg width="18" height="18" viewBox="0 0 24 24" aria-hidden="true">
        <path fill="#4f9a4a" d="M6.6 10.8a15.1 15.1 0 0 0 6.6 6.6l2.2-2.2a1 1 0 0 1 1-.25 11.4 11.4 0 0 0 3.6.57 1 1 0 0 1 1 1V20a1 1 0 0 1-1 1A17 17 0 0 1 3 4a1 1 0 0 1 1-1h3.5a1 1 0 0 1 1 1c0 1.25.2 2.45.57 3.6a1 1 0 0 1-.25 1z"/>
      </svg>
      <span class="divider"></span>
      <ul>
        <li>Spain (+34) 612 480 397</li>
        <li>(USA) +1 (555) 318 2046</li>
      </ul>
    </div>
  </section>
</body>
</html>
```